Norwegian psychologist service needs a fresh and exiting web site*

Norwegian psychologist service: working with therapy, personal development, mastery and personal growth. Focus: children and teenagers with special needs; family dynamics; group processes; individuals with a need for therapy and personal growth. (Our company name: Fjordlys og samhold (means Mastery and Growth).

We already have a logo for the company, which will be used (will be attached in the project).

The webside is to be structured in 4 pages with roll down curtain menus (the numbers are just for guiding the designer - the should not be added):

Page 1: Om Fjordlys og Samhold (about Mastery and Growth): this is where our business is is presented/described shortly: Lorem Ipsum dolor cit...

Page 2: Tjenester (Services): this is where our 5 service areas are presented:
2.1 Utredning (Investigation, diagnosing): Lorem Ipsum dolor cit...
2.2 Rådgivning (consulting): Lorem Ipsum dolor cit...

2.3 Kurs og work shops (courses and work shops): Lorem Ipsum dolor cit...
2.3a Fjordlys og samhold Tema 1 (T1)
2.3b Fjordlys og samhold Tema 2 (T2)
2.3c Fjordlys og samhold Tema 3 (T3)

2.4 Terapi og utvikling (Therapy and development)
2.4a Fjordlys og samhold for individer (FS1)
2.4b Fjordlys og samhold i familier (FS2)
2.4c Fjordlys og samhold i grupper (FS3)
2.4d Fjordlys og samhold i institusjoner (FS4)

Page 3: Aktuelt (Blog): this is our blog where we share knowledge and articles

Page 4: Kontakt (Contact): This is the contact form page. Contact form should constitute:
- Ditt navn (your name)
- E-post (your e-mail)
- Emne (subject)
- Melding (message/description)

Our project should also include suggestion for handheld units (iPhone, iPad).
Updates

We have both been traveling with work for a while, and then unfortunately both of us got sick on return, so we need a few more days to evaluate and choose design. Kind Regards Arvid & Margit

Target Market(s)

Focus on therapy, learning, mastery and growth for children and teenagers with special needs, within the family dynamics, or in a group setting.
OUR MARKETS:
Private market: individuals, families, groups and health industry institutions (with focus on learning, mastery, growth (as well as growing up) and psychiatry for children and teenagers with special difficulties and needs)
Public institutions: Government institutions, state institutions and municipality institutions (e.g. schools, municipality health service, hospitals) that serve the public (families with children and teenagers with special needs, and where learning, mastery, growth (as well as growing up) and potential psychiatry is an issue).

Number of Pages Required

4 page

Font styles to use
Sans Serif

Colors

Designer to choose colors to be used in the design.

Requirements
Must have
• The website must have 4 pages with roll down curtain menus (we have added a PDF with suggested structure, and headings, with sub menus - see attached PDF drawing.
• The web page must also use the added logo file - and make the web page work well with our logo.
• We would like the website to have a modern look and we would like the site to be associated with typical HIGH END TOP QUALITY private health institutions, but with a stronger focus on human beings (hands, faces etc), and not white coats and doctors. We are psychologists in the private market.
• For instance, if photos are being used - we tend to like "warm" almost art-like, "grainy" two-tone (e.g. sepia) photos to illustrate our focus. If designer can find such photos as part of design, it would be interesting to us. We would like a few photos like that integrated in the design.
• We also want a design suggestion for how the web page should look like and behave on handheld units (e.g. iPhone, iPad).
Nice to have
• If designer could find a number of suitable photos that matches the business idea and design requirements (see description above), that could follow website, that would be good.
• It could also be nice to have graphic symbols that denote the different pages/subpages (subjects)....
• HORSES: we sometimes use horses as a "tool" in therapy sessions. The horse is not necessarily used for riding, but for contact, communication and grooming. PHOTOS: we would like the designer to find an opportunity for using a photo reflecting this cooperation between therapist, child, teenager and horse. It is a bit up to the designer to find a way to do this... Since the horse is only a tool, among many other tools, it does not have to be much - but we want to try and see how it will work with a photo that also reflects this part of our business.

```html
<!DOCTYPE html>
<html lang="no">
<head>
<meta charset="utf-8">
<title>Om Fjordlys og Samhold</title>
<link href="https://fonts.googleapis.com/css2?family=Roboto+Slab:wght@300;400;700&family=Zilla+Slab:wght@300;400;700&family=Lora:ital,wght@1,400&display=swap" rel="stylesheet">
<style>
:root{
  --blue:#2b3990;
  --green:#0d6b3a;
  --plum:#7a7490;
  --text:#707070;
  --canvas:#ededed;
  --white:#ffffff;
  --slab:"Roboto Slab","Zilla Slab","Rockwell","Courier New",serif;
}
*{box-sizing:border-box;margin:0;padding:0}
html,body{width:1200px;height:3889px;overflow:hidden;background:var(--canvas)}
body{font-family:var(--slab);color:var(--text);position:relative}
.page{position:absolute;left:50px;top:51px;width:1108px;height:3787px;background:var(--white);box-shadow:0 0 20px rgba(0,0,0,.06)}
.abs{position:absolute}
.photo{position:absolute}

/* hero */
.hero{left:50px;top:51px;width:1108px;height:788px;
  background:linear-gradient(170deg,#6b6a66 0%,#8a8378 25%,#6c6c6a 45%,#4e5253 65%,#474848 100%)}
.hero::after{content:"";position:absolute;inset:0;background:linear-gradient(200deg,rgba(214,184,154,.75) 0%,rgba(214,184,154,0) 45%)}
.brand{position:absolute;display:flex;align-items:center;gap:10px;color:var(--white);font-family:var(--slab);font-weight:400;font-size:16px;white-space:nowrap;z-index:2}
.brand .dot{width:22px;height:22px;border-radius:50%;background:currentColor;flex:none}
.nav a{position:absolute;color:var(--white);font-size:14.5px;font-weight:700;text-decoration:none;top:114px}
.nav .active::after{content:"";position:absolute;left:-4px;right:-4px;bottom:-10px;height:2px;background:var(--white)}
.social{position:absolute;display:flex;gap:18px}
.social span{width:20px;height:20px;border-radius:50%;border:2px solid var(--white)}
.hero-title{position:absolute;left:50px;width:1108px;top:388px;text-align:center;color:var(--white);font-weight:700;font-size:52px;z-index:2}
.hero-rule{position:absolute;top:478px;height:2px;z-index:2}
.hero-copy{position:absolute;left:386px;top:500px;width:460px;color:var(--white);font-weight:300;font-size:15px;line-height:23px;z-index:2}
.pill{position:absolute;display:flex;align-items:center;justify-content:space-between;border:2px solid var(--white);border-radius:22px;color:var(--white);font-size:14.5px;padding:0 5px 0 22px;z-index:2;text-decoration:none}
.pill .go{width:30px;height:30px;border-radius:50%;display:flex;align-items:center;justify-content:center}

/* blog strip */
.blog{left:157px;top:737px;width:893px;height:173px;background:var(--plum);border-radius:3px;overflow:hidden;z-index:3}
.blog .accent{position:absolute;left:0;top:0;width:326px;height:100%;background:var(--blue)}
.post-img{position:absolute;top:34px;width:171px;height:103px}
.post-text{position:absolute;top:30px;width:200px;color:var(--white)}
.post-text h3{font-size:15px;font-weight:400;margin-bottom:4px}
.post-text p{font-size:10.5px;line-height:15px;font-weight:300;opacity:.85}
.post-text .more{display:block;margin-top:22px;font-size:11px;font-weight:700}

/* sections */
.section-head{position:absolute;display:flex;align-items:center;gap:12px;color:var(--blue);font-weight:700;font-size:26px}
.section-head::before{content:"";width:77px;height:2px;background:var(--blue)}
.body-copy{position:absolute;font-size:14.5px;line-height:23px;font-weight:300;color:var(--text)}
.body-copy p{margin-bottom:8px}
.leaf{display:inline-block;width:20px;height:9px;border-radius:0 100% 0 100%;background:var(--green);vertical-align:middle;margin-left:6px}
.quote{position:absolute;font-family:"Lora",Georgia,serif;font-style:italic;font-size:26px;line-height:27px}
.quote .mark{position:absolute;left:-40px;top:-2px;font-size:44px;font-weight:700}

.person h4{color:var(--blue);font-size:15px;font-weight:700}
.person .mail{font-size:10.5px;margin:4px 0 10px}
.person .role{font-size:15px;font-weight:400;color:#555;margin-bottom:14px}

/* footer */
.footer{left:50px;top:3535px;width:1108px;height:303px;background:var(--plum)}
.footer-col{position:absolute;color:var(--white)}
.footer-col h5{font-size:14.5px;font-weight:700;margin-bottom:16px}
.footer-col li{list-style:none;font-size:11.5px;line-height:23px;font-weight:300}
</style>
</head>
<body>
<div class="page"></div>

<header class="abs hero" role="img" aria-label="Soft photograph of rippling water in warm sepia and grey tones"></header>
<div class="brand" style="left:155px;top:140px"><span class="dot"></span>Fjordlys og samhold</div>
<nav class="nav" style="z-index:2;position:relative">
  <a class="active" href="#" style="left:515px">Tjenester</a>
  <a href="#" style="left:623px">Aktuelt</a>
  <a href="#" style="left:845px">Kontakt</a>
</nav>
<div class="social" style="left:954px;top:113px;z-index:2"><span></span><span></span><span></span></div>

<h1 class="hero-title">Om Fjordlys og Samhold</h1>
<div class="hero-rule" style="left:158px;width:159px;background:rgba(255,255,255,.25)"></div>
<div class="hero-rule" style="left:317px;width:98px;background:var(--green)"></div>
<div class="hero-rule" style="left:415px;width:177px;background:var(--white)"></div>
<p class="hero-copy">Our mission is to maintain high quality of psychological services by selecting proven specialists; to increase confidence in psychology in general and prevent its discrediting, as well as to improve psychological literacy of users.</p>
<a class="pill" href="#" style="left:386px;top:619px;width:206px;height:41px">You can write us
  <span class="go" style="background:var(--green)"><svg width="14" height="14" viewBox="0 0 14 14"><path d="M2 7h10M8 3l4 4-4 4" stroke="#fff" stroke-width="1.8" fill="none"/></svg></span></a>

<section class="abs blog">
  <div class="accent"></div>
  <div class="post-img" style="left:35px;background:linear-gradient(135deg,#a47c55,#6d5a44 60%,#b49a7a)" role="img" aria-label="Photo of a horse with a long mane in a field"></div>
  <div class="post-text" style="left:229px">
    <h3>Blog News</h3>
    <p>Praesent lacus nunc, feugiat quis diam quis, condimentum eleifend arcu.Pellentesque vulputate non...</p>
    <span class="more">Read more &nbsp;›</span>
  </div>
  <div class="post-img" style="left:469px;background:linear-gradient(180deg,#b8b2a4,#6e6d55 60%,#4d5140)" role="img" aria-label="Photo of a misty forest by a lake"></div>
  <div class="post-text" style="left:664px">
    <h3>Blog News</h3>
    <p>Hasellus maximus, enim id vehicula commodo, augue nunc euismod ipsum, et aliquet nisl dolor sed...</p>
    <span class="more">Read more &nbsp;›</span>
  </div>
</section>

<div class="brand" style="left:386px;top:1130px;color:var(--blue);font-size:26px;gap:14px"><span class="dot" style="width:38px;height:38px"></span>Fjordlys og samhold</div>

<h2 class="section-head" style="left:157px;top:1252px">About Us</h2>
<div class="body-copy" style="left:388px;top:1255px;width:450px">
  <p>Lorem ipsum dolor sit amet, consectetur adipiscing elit. Etiam viverra ullamcorper est, nec cursus metus faucibus eu. Nunc non nisi eu odio elementum iaculis. Duis feugiat orci ac turpis varius, eget aliquam risus consequat.</p>
  <p>Mauris non ex mauris. Donec id ligula rutrum, molestie eros et, malesuada eros. Praesent porta odio sit amet tellus iaculis auctor. Nulla facilisi. Praesent at tempus ipsum. Fusce lobortis cursus tortor quis sodales.</p>
  <p>Curabitur euismod, quam quis volutpat efficitur, magna odio tristique lorem, nec mollis orci lorem in erat. Etiam hendrerit nec nisl sed luctus. Proin gravida venenatis quam. Mauris luctus tincidunt metus. In sit amet luctus risus.<span class="leaf"></span></p>
</div>

<div class="photo" style="left:50px;top:1656px;width:567px;height:265px;background:linear-gradient(135deg,#3f7a72,#2f5f5a 40%,#5e8d83 70%,#3c6b64)" role="img" aria-label="Photo of sunlit water ripples in teal"></div>
<div class="photo" style="left:157px;top:1656px;width:77px;height:265px;background:var(--blue)"></div>
<div class="photo" style="left:617px;top:1656px;width:433px;height:265px;background:radial-gradient(circle at 50% 45%,#7fb3b0 0%,#4b6e5a 35%,#5a3f2c 80%)" role="img" aria-label="Photo looking up at tall tree trunks toward the sky"></div>
<blockquote class="quote" style="left:258px;top:1736px;width:320px;color:var(--white)"><span class="mark">“</span>Everything that exists in the universe, the organic and inorganic world.</blockquote>

<h2 class="section-head" style="left:527px;top:2028px">Founders</h2>
<div class="photo" style="left:386px;top:2092px;width:206px;height:192px;background:linear-gradient(160deg,#6e5a45,#a48d6e 55%,#5b4b3a)" role="img" aria-label="Photo of a woman in a knitted hat looking over a valley"></div>
<div class="abs person" style="left:614px;top:2090px;width:430px">
  <h4>Ingrid Solberg</h4>
  <div class="mail">post@fjordlys-samhold.no</div>
  <div class="role">Practicing Psychologist</div>
  <div class="body-copy" style="position:static">
    <p>Lorem ipsum dolor sit amet, consectetur adipiscing elit. Etiam viverra ullamcorper est, nec cursus metus faucibus eu. Nunc non nisi eu odio elementum iaculis. Duis feugiat orci ac turpis varius, eget aliquam risus consequat.</p>
    <p>Mauris non ex mauris. Donec id ligula rutrum, molestie eros et, malesuada eros. Praesent porta odio sit amet tellus iaculis auctor. Nulla facilisi. Praesent at tempus ipsum. Fusce lobortis cursus tortor quis sodales.</p>
  </div>
</div>

<div class="photo" style="left:157px;top:2415px;width:206px;height:192px;background:linear-gradient(120deg,#2e2418,#6b5236 50%,#3a2d1f)" role="img" aria-label="Warm-toned portrait photo of a bearded man with glasses"></div>
<div class="abs person" style="left:386px;top:2413px;width:400px">
  <h4>Tore Lindhaug</h4>
  <div class="mail">post@fjordlys-samhold.no</div>
  <div class="role">Practicing Psychologist</div>
  <div class="body-copy" style="position:static">
    <p>Mauris non ex mauris. Donec id ligula rutrum, molestie eros et, malesuada eros. Praesent porta odio sit amet tellus iaculis auctor. Nulla facilisi. Praesent at tempus ipsum. Fusce lobortis cursus tortor quis sodales.</p>
  </div>
</div>

<div class="photo" style="left:845px;top:2607px;width:205px;height:533px;background:linear-gradient(180deg,#5a4631,#c2a47e 40%,#8a6f52 70%,#4a3a2a)" role="img" aria-label="Photo of two people walking in a sunlit forest"></div>
<h2 class="section-head" style="left:296px;top:2712px">Why are we doing this?</h2>
<div class="body-copy" style="left:386px;top:2772px;width:422px">
  <p>Lorem ipsum dolor sit amet, consectetur adipiscing elit. Etiam viverra ullamcorper est, nec cursus metus faucibus eu. Nunc non nisi eu odio elementum iaculis. Duis feugiat orci ac turpis varius, eget aliquam risus consequat.</p>
  <p>Mauris non ex mauris. Donec id ligula rutrum, molestie eros et, malesuada eros. Praesent porta odio sit amet tellus iaculis auctor. Nulla facilisi. Praesent at tempus ipsum. Fusce lobortis cursus tortor quis sodales.</p>
  <p>Curabitur euismod, quam quis volutpat efficitur, magna odio tristique lorem, nec mollis orci lorem in erat. Etiam hendrerit nec nisl sed luctus.</p>
  <p>Proin gravida venenatis quam. Mauris luctus tincidunt metus. In sit amet luctus risus.<span class="leaf"></span></p>
</div>

<div class="photo" style="left:157px;top:3195px;width:436px;height:224px;background:linear-gradient(135deg,#3d4236,#6b5a43 50%,#8c7a62 80%,#4a4638)" role="img" aria-label="Photo of a bird of prey landing on rocks"></div>
<blockquote class="quote" style="left:654px;top:3283px;width:330px;color:var(--plum)"><span class="mark">“</span>Everything that exists in the universe, the organic and inorganic world.</blockquote>

<footer class="abs footer">
  <div class="abs" style="left:336px;top:0;width:206px;height:10px;background:var(--blue)"></div>
  <div class="abs" style="left:542px;top:0;width:566px;height:10px;background:var(--green)"></div>
</footer>
<div class="brand" style="left:155px;top:3665px"><span class="dot"></span>Fjordlys og samhold</div>
<div class="footer-col" style="left:386px;top:3600px">
  <h5>Tjenester</h5>
  <ul>
    <li>Utredning</li>
    <li>Rådgivning (consulting):</li>
    <li>Kurs og workshops</li>
    <li>Fjordlys og samhold (T1, T2, T3)</li>
    <li>Terapi og utvikling</li>
    <li>Fjordlys og samhold for individer (FS1-FS4)</li>
  </ul>
</div>
<div class="footer-col" style="left:619px;top:3600px"><h5>Aktuelt</h5></div>
<div class="footer-col" style="left:845px;top:3600px"><h5>Kontakt</h5></div>
<div class="social" style="left:845px;top:3640px"><span></span><span></span><span></span></div>
<a class="pill" href="#" style="left:844px;top:3721px;width:205px;height:42px;font-weight:300;color:rgba(255,255,255,.85)">You can write us
  <span class="go" style="background:var(--white)"><svg width="14" height="14" viewBox="0 0 14 14"><path d="M2 7h10M8 3l4 4-4 4" stroke="#7a7490" stroke-width="1.8" fill="none"/></svg></span></a>
</body>
</html>
```